Delta Ridge Arms

Firearms Website

Requirements
Must have
• we are looking for two or three pages for a new company we are starting. The Name is Delta Ridge Arms. The site will be DeltaRidgeArms.example (nothing on site at this time) We will be selling mainly handguns and products for self defense. We want this site to focus on the handgun and ammo sells as well as low cost transfers. we will handle the ecommerce part) We want a

1.) main page, mainly general information on the company.

2.) a page for sells. we will be adding the guns by hand as we place them for sell and use our credit card process. We just need the layout to fill in the items for sale on this page.

3.) navigation will be.. HOME - SALES (((guns and gun Accessories)) and self defense products) - Contact US- Transfers

company info

Delta Ridge Arms

DeltaRidgeArms.example

sales@DeltaRidgeArms.example

855-Bolt 2 Save (855-265-2728) same number for fax

412 south Walnut street

Kosciusko, ms. 39090

```html
<!DOCTYPE html>
<html lang="en">
<head>
<meta charset="utf-8">
<title>Delta Ridge Arms</title>
<link href="https://fonts.googleapis.com/css2?family=PT+Sans+Narrow:wght@400;700&family=PT+Sans:wght@400;700&family=Ubuntu:wght@500&display=swap" rel="stylesheet">
<style>
:root{
  --ink:#222;
  --text:#4a4a4a;
  --header:#2d2d2d;
  --gold:#e8c24a;
  --gold-light:#efd46a;
  --gold-deep:#dca51e;
  --white:#fff;
  --line:#dcdcdc;
  --btn-gold:#d9b45a;
  --photo-dark:#2b2b2e;
  --photo-mid:#5a5a5e;
}
*{margin:0;padding:0;box-sizing:border-box}
html,body{width:918px;height:1200px;overflow:hidden}
body{position:relative;background:var(--white);font-family:"PT Sans",sans-serif;color:var(--text)}
.abs{position:absolute}
.heading{font-family:"PT Sans Narrow",sans-serif;font-weight:700;color:var(--ink)}

.site-header{left:0;top:0;width:918px;height:112px;background:linear-gradient(#3a3a3a 0 5px,var(--header) 5px)}
.brand{left:54px;top:30px;font-family:"Ubuntu",sans-serif;font-weight:500;color:var(--gold);font-size:25px;line-height:27px}
.phone{right:57px;top:16px;text-align:right;color:var(--gold);font-family:"PT Sans",sans-serif;font-size:15px;line-height:20px}
.phone svg{vertical-align:-2px;margin-right:4px}
.main-nav{right:59px;top:77px;display:flex;font-family:"PT Sans",sans-serif;font-weight:700;font-size:15px;color:var(--white)}
.main-nav span{padding:0 18px;border-left:1px solid #777;line-height:16px}
.main-nav span:first-child{border-left:0}
.main-nav span:last-child{padding-right:0}

.hero{left:0;top:112px;width:918px;height:340px;background:linear-gradient(var(--gold-light),var(--gold-deep))}
.hero-title{left:59px;top:56px;font-size:30px}
.hero-sub{left:60px;top:92px;font-family:"PT Sans Narrow",sans-serif;font-weight:700;font-size:17px;color:#2a2a2a}
.hero-text{left:60px;top:120px;width:340px;font-size:10.6px;line-height:19.5px;color:#2d2d2d}
.btn-dark{left:59px;top:192px;width:106px;height:29px;background:#111;border-radius:3px;color:var(--white);font-family:"PT Sans Narrow",sans-serif;font-weight:700;font-size:13px;text-align:center;line-height:29px}
.hero-dots{left:61px;top:249px;display:flex;gap:2px}
.hero-dots i{width:6px;height:6px;border-radius:50%;background:#7a5a10}
.hero-dots i:first-child{background:var(--white)}
.hero-frame{left:433px;top:30px}

.our-guns{left:0;top:452px;width:918px;height:170px;background:linear-gradient(var(--white),#f0f0f0)}
.section-title{font-size:18px}
.thumbs{left:54px;top:50px;display:flex;gap:19px}
.thumb{width:148px;height:86px;border:2px solid var(--white);box-shadow:0 0 3px rgba(0,0,0,.25);background:linear-gradient(135deg,var(--photo-mid),var(--photo-dark) 70%)}

.welcome{left:54px;top:646px;width:548px}
.welcome h2,.blog h2{font-size:20px;margin-bottom:10px}
.lead{font-weight:700;font-size:10px;line-height:18px;color:#333;margin-bottom:7px}
.body-copy{font-size:10px;line-height:18px;margin-bottom:6px}
.blog{left:633px;top:646px;width:240px}
.blog h3{font-size:10.2px;font-weight:700;color:#333;line-height:18px}
.blog p{font-size:10px;line-height:18px;margin-bottom:15px}

.divider{left:41px;top:888px;width:837px;height:1px;background:var(--line)}

.feature{top:916px;width:260px}
.feature h2{font-size:18px;margin-bottom:6px}
.feature-img{position:absolute;left:0;top:28px;width:98px;height:108px}
.feature-body{margin-left:106px}
.feature-body h3{font-size:10.2px;font-weight:700;color:#333;line-height:18px}
.feature-body p{font-size:10px;line-height:18px}
.btn-gold{position:absolute;left:106px;top:142px;width:67px;height:24px;border-radius:3px;background:linear-gradient(#e6c676,var(--btn-gold));color:#4a3710;font-size:9px;font-weight:700;text-align:center;line-height:24px;box-shadow:0 1px 1px rgba(0,0,0,.2)}

.site-footer{left:0;top:1126px;width:918px;height:74px;background:linear-gradient(#e8e8e8,#fbfbfb 30%,#f3f3f3)}
.copyright{left:56px;top:24px;font-size:9.5px;color:#555}
.footer-nav{left:498px;top:24px;font-size:9.6px;font-weight:700;color:#444}
.footer-nav b{font-weight:400;margin:0 6px}
.social{left:795px;top:19px;display:flex;gap:4px}
.social i{width:21px;height:21px;border-radius:50%;background:#111}
</style>
</head>
<body>
<header class="site-header abs">
  <div class="brand abs">Delta Ridge<br>Arms</div>
  <div class="phone abs">855-Bolt 2 Save<br><svg width="11" height="12" viewBox="0 0 12 12"><path d="M2.5 1 L4.5 3.5 L3.5 5 Q5 7.5 7 8.5 L8.5 7.5 L11 9.5 L9.5 11.5 Q4 11 0.5 2.5 Z" fill="#e8c24a"/></svg>855-265-2728</div>
  <nav class="main-nav abs"><span>Home</span><span>Sales</span><span>Self Defence</span><span>Contact us</span><span>Transfers</span></nav>
</header>

<section class="hero abs">
  <h1 class="hero-title heading abs">Buy Best Mississippi Firearms</h1>
  <div class="hero-sub abs">Lorem ipsum dolor sit consectetuer adipiscing elit.</div>
  <p class="hero-text abs">Pellentesque habitant morbi tristique senectus et netus et malesuada fames ac turpis egestas. Cras id elit. Integer quis urna. Ut ante enim, dapibus malesuada, fringilla eu, condimentum quis, tellus.</p>
  <div class="btn-dark abs">VIEW ALL GUNS</div>
  <div class="hero-dots abs"><i></i><i></i><i></i><i></i></div>
  <svg class="hero-frame abs" width="437" height="276" viewBox="0 0 437 276" role="img" aria-label="Featured photo of a silver pistol with a holster and ammunition">
    <defs><linearGradient id="heroPhoto" x1="0" y1="0" x2="1" y2="1"><stop offset="0" stop-color="#6a6a70"/><stop offset=".5" stop-color="#3a3a40"/><stop offset="1" stop-color="#1c1c20"/></linearGradient></defs>
    <path d="M0 0H437V276H48L0 228Z" fill="#111"/>
    <path d="M7 7H430V268H52L7 223Z" fill="url(#heroPhoto)"/>
  </svg>
</section>

<section class="our-guns abs">
  <h2 class="section-title heading abs" style="left:53px;top:20px">Our Guns</h2>
  <div class="thumbs abs">
    <div class="thumb" role="img" aria-label="Photo of a pistol with cartridges"></div>
    <div class="thumb" role="img" aria-label="Photo of a semi-automatic pistol"></div>
    <div class="thumb" role="img" aria-label="Photo of a handgun with loose rounds"></div>
    <div class="thumb" role="img" aria-label="Photo of a black pistol"></div>
    <div class="thumb" role="img" aria-label="Photo of a pistol on a display case"></div>
  </div>
</section>

<section class="welcome abs">
  <h2 class="heading">Welcome to Our Website Mainpage..</h2>
  <p class="lead">Lorem ipsum dolor sit amet, consectetuer adipiscing elit. Nam cursus. Morbi ut mi. Nullam enim leo, egestas id, condimentum at, laoreet mattis, massa. Sed eleifend nonummy diam.</p>
  <p class="body-copy">Praesent mauris ante, elementum et, bibendum at, posuere sit amet, nibh. Duis tincidunt lectus quis dui viverra vestibulum. Suspendisse vulputate aliquam dui. Nulla elementum dui ut augue. Aliquam vehicula mi at mauris. Maecenas placerat, nisl at consequat rhoncus, sem nunc gravida justo, quis eleifend arcu velit quis lacus.</p>
  <p class="body-copy">Pellentesque habitant morbi tristique senectus et netus et malesuada fames ac turpis egestas. In posuere felis nec tortor. Pellentesque faucibus. Ut accumsan ultricies elit. Maecenas at justo id velit placerat molestie. Donec dictum lectus non odio. Cras a ante vitae enim iaculis aliquam. Mauris nunc quam, venenatis nec, euismod sit amet, egestas placerat, est. Pellentesque habitant morbi tristique senectus et netus et malesuada fames ac turpis egestas.</p>
</section>

<aside class="blog abs">
  <h2 class="heading">Recent Blog Post</h2>
  <h3>Donec convallis pede venenatis nibh.</h3>
  <p>Felis vestibulum volutpat. Etiam est nunc, venenatis in, tristique eu, imperdiet ac, nisl.</p>
  <h3>Mauris vel lacus vitae</h3>
  <p>Cum sociis natoque penatibus et magnis dis</p>
  <h3>Donec convallis pede venenatis nibh.</h3>
  <p>parturient montes, nascetur ridiculus mus. In iaculis facilisis massa. Etiam eu urna. Sed porta.</p>
</aside>

<div class="divider abs"></div>

<section class="feature abs" style="left:62px">
  <h2 class="heading">About Our Products</h2>
  <div class="feature-img" role="img" aria-label="Photo of a revolver with bullets" style="background:linear-gradient(135deg,#f2f2f2,#a8a8ac)"></div>
  <div class="feature-body"><h3>Donec convallis pede</h3><p>Ut ante enim, dapibus malesuada, fringilla eu, condimentum quis, tellus. Aenean porttitor eros vel dolor. Donec convallis pede venenatis nibh.</p></div>
  <div class="btn-gold">Learn More</div>
</section>

<section class="feature abs" style="left:334px">
  <h2 class="heading">How to Buy?</h2>
  <div class="feature-img" role="img" aria-label="Photo of a pistol resting on banknotes" style="background:linear-gradient(135deg,#8a7a86,#2a2a2c 60%)"></div>
  <div class="feature-body"><h3>Donec convallis pede</h3><p>Ut ante enim, dapibus malesuada, fringilla eu, condimentum quis, tellus. Aenean porttitor eros vel dolor. Donec convallis pede venenatis nibh.</p></div>
  <div class="btn-gold">Learn More</div>
</section>

<section class="feature abs" style="left:607px">
  <h2 class="heading">Self Defence</h2>
  <div class="feature-img" role="img" aria-label="Photo of a woman holding a handgun" style="background:linear-gradient(90deg,#111 40%,#6a5446)"></div>
  <div class="feature-body"><h3>Donec convallis pede</h3><p>Ut ante enim, dapibus malesuada, fringilla eu, condimentum quis, tellus. Aenean porttitor eros vel dolor. Donec convallis pede venenatis nibh.</p></div>
  <div class="btn-gold">Learn More</div>
</section>

<footer class="site-footer abs">
  <div class="copyright abs">© 2012 Company Name.&nbsp; All right reserved.&nbsp; Term of Use</div>
  <div class="footer-nav abs">Home<b>/</b>Sales<b>/</b>Self Defence<b>/</b>Contact us<b>/</b>Transfers</div>
  <div class="social abs"><i></i><i></i><i></i></div>
</footer>
</body>
</html>
```